" ESCRITORIO DE SERVICO CONSULTIVO PROVIDO POR PROFISSIONAIS COM AMPLA EXPERIENCIA NO SETOR ELETRICO COM ATUACAO ACIMA DE 13 ANOS DE EXPERIENCIA. ATUMOS ATRAVES DO ENGAJAMENTO DE AGENTES A PARTIR DE CONSULTA DA NECESSIDADE E ELABORACAO DE PACOTE DE SERVICOS ALINHADO A EXPECTATIVA DO CLIENTE. SERVICOS PRINCIPAIS: GESTAO DE PLEITOS DE CONTRATOS DE GERACAO, TRANSMISSAO E DISTRIBUICAO DE ENERGIA GESTAO DE PROCESSOS DE AQUISICAO DE EQUIPAMENTOS E SERVICOS PARA EMPREENDIMENTOS DE GERACAO, TRANSMISSAO E DISTRIBUICAO DE ENERGIA OUTROS SERVICOS: PLANEJAMENTO E GESTAO DE EMPREENDIMENTOS DE GERACAO, TRANSMISSAO E DISTRIBUICAO DE ENERGIA "

```html
<!DOCTYPE html>
<html lang="pt-BR">
<head>
<meta charset="UTF-8">
<title>Voltare Consultoria – Papelaria</title>
<link href="https://fonts.googleapis.com/css2?family=Michroma&family=Roboto:wght@400&display=swap" rel="stylesheet">
<style>
  :root {
    --bg: #e9eaec;
    --paper: #ffffff;
    --paper-shade: #eeeff1;
    --amber: #e7a617;
    --ink: #3a3d42;
    --ink-soft: #5f636a;
    --band-light: #f4f4f5;
    --band-dark: #c9cbce;
    --spine: #2b2d31;
  }
  * { box-sizing: border-box; margin: 0; padding: 0; }
  html, body { width: 1200px; height: 1200px; overflow: hidden; background: var(--bg); }
  .stage { position: relative; width: 1200px; height: 1200px; }

  .wordmark { font-family: "Michroma", sans-serif; color: var(--ink); text-align: center; line-height: 1; }
  .wordmark .name { display: block; letter-spacing: 0.08em; }
  .wordmark .tag { display: block; letter-spacing: 0.55em; margin-top: 6px; }

  /* Letterhead */
  .letterhead {
    position: absolute; left: 80px; top: 250px; width: 480px; height: 680px;
    background: var(--paper); box-shadow: 0 10px 30px rgba(0,0,0,.12);
  }
  .letterhead .header { position: absolute; top: 50px; left: 0; right: 0; display: flex; flex-direction: column; align-items: center; gap: 12px; }
  .letterhead .dot { width: 22px; height: 22px; border-radius: 50%; background: var(--amber); }
  .letterhead .wordmark .name { font-size: 22px; }
  .letterhead .wordmark .tag { font-size: 7px; }
  .letterhead .accent { position: absolute; left: 150px; top: 230px; width: 180px; height: 180px; border-radius: 50%; background: var(--amber); }
  .letterhead .footer {
    position: absolute; left: 0; right: 0; bottom: 0; height: 110px;
    background: linear-gradient(90deg, var(--band-dark), var(--band-light) 70%);
    padding: 18px 28px 0 0; text-align: right;
    font-family: "Roboto", sans-serif; font-size: 11.5px; color: var(--ink-soft); line-height: 1.45;
  }
  .letterhead .social { display: inline-flex; align-items: center; gap: 5px; margin-left: 10px; }
  .letterhead .social i { width: 10px; height: 10px; background: var(--ink-soft); display: inline-block; }

  /* Folder */
  .folder {
    position: absolute; left: 610px; top: 200px; width: 520px; height: 760px;
    background: linear-gradient(160deg, var(--paper), var(--paper-shade));
    border-right: 10px solid var(--spine);
    box-shadow: 0 12px 34px rgba(0,0,0,.16);
  }
  .folder .accent { position: absolute; left: 130px; top: 170px; width: 250px; height: 250px; border-radius: 50%; background: var(--amber); }
  .folder .band {
    position: absolute; left: 0; right: 0; top: 560px; height: 110px;
    background: linear-gradient(90deg, var(--band-light), var(--band-dark));
    display: flex; align-items: center; justify-content: flex-end; padding-right: 50px;
  }
  .folder .wordmark .name { font-size: 28px; }
  .folder .wordmark .tag { font-size: 8px; }
</style>
</head>
<body>
<main class="stage">
  <section class="letterhead" aria-label="Papel timbrado">
    <header class="header">
      <span class="dot"></span>
      <div class="wordmark"><span class="name">VOLTARE</span><span class="tag">CONSULTORIA</span></div>
    </header>
    <div class="accent"></div>
    <footer class="footer">
      <p>www.voltare.com.br</p>
      <p>Rua do Projeto, 00 - cidade - Estado - SP - 00000-000</p>
      <p>(11) 0000-0000 | contato@voltare.com.br</p>
      <p><span class="social"><i></i>voltare</span><span class="social"><i></i>@voltare</span></p>
    </footer>
  </section>

  <section class="folder" aria-label="Pasta institucional">
    <div class="accent"></div>
    <div class="band">
      <div class="wordmark"><span class="name">VOLTARE</span><span class="tag">CONSULTORIA</span></div>
    </div>
  </section>
</main>
</body>
</html>
```